2-Page Flyer for the Information Session about the Quiet Venture Pathway

This is a flyer to announce/advertise an evening Information Session about the Quiet Venture Pathway. This Program aims at mindfully rethinking and redesigning work (and life) for people who feel stuck or not entirely satisfied with their work and/or life (please see draft flyer attached for more details). This Program is property of Bright Meadow, a company that uses a combination of Mindfulness, Design, and Entrepreneurship to help people achieve greater happiness (in their work and lives).
Updates

Target Market(s)

People who feel stuck or not entirely satisfied with their work and/or life (please see draft flyer attached for more details)

Font styles to use
Serif
Sans Serif

Colors
ffffff
f37122
33a6d7
acd037

Requirements
Must have
• All of what I will say below is suggestive (I’m not a design expert), and I’m open to divert from it, if it makes sense and feels more interesting.
• I thought initially of a 2-page flyer (please see draft flyer attached). The first page could help people grasp the essence of the event quickly (in 1 or 2 minutes), and then, if they are interested/motivated, they would continue reading through page 2, which has more info about the Program in itself.
• Potential Structure
• Page 1
• . About the Information Session on the Quiet Venture Pathway
• . Visible Date & Time, Contacts, Venue (and other relevant info)
• . About me (the facilitator)
• Page 2
• . About the Quiet Venture Pathway
• I include a Powerpoint draft of the flyer with the content. The design is rudimentary and precarious from an aesthetics/organization point of view, and this is mainly where I need help (and maybe in other aspects too!).
• On the flyer, I would like to include:
• . A photo of myself (I attach 1 picture).
• . 1 or 2 beautiful-nature photos (cropped or full). One may have to do with looking at the sky, dreaming, and imagining a new work and life (2 photos with sky and clouds attached). The other has to do with walking the transformation journey (the photo with the person walking through the forest path).
• . bright meadow logo or logos (there are two slightly different ones, that can be used for different purposes). For the first page, I would like the bright meadow logo that has "bright meadow" written on the bottom, with the saying "Calm, Craft and Enterprise for Joyful Living" beneath. This is the main logo. For the 2nd page, you can choose the logo that adapts better.
• - Where it says the "the way out is in" it would be great to have a similar font to the one I attach (see file "Font_the_way_out_is_in.png" and Torvenscript-qr.ttf
Nice to have
• In terms of colours, I would not divert much from the logo colours (and of course white and black). I would like the flyer to be quite white. Almost like fairy-tale white: the white horse, the white snow, the white of the stars, the white heaven. White could be the base colour. White means peace, tranquillity, calm contentment, a smile.
• And then use the other colours. The green of the mindfulness. The blue of the sky, the dreams. And the orange of the sun, the energy, the fire, the action. And maybe the black for text.
• Where it says the "the way out is in" it would be great to have a similar font to the one I attach (see file "Font_the_way_out_is_in".
• I would like this flyer to be a piece of art, in every possible way. Simple, beautiful, ease, light, peaceful, calm happy. Just like the Quiet Venture Pathway and bright meadow Company that I am creating intends to be. The mission of this Program and Company is to be a designer, a painter (a Picasso) of happier and more fulfilling human lives.
• I am very much looking forward to seeing your proposal(s).

```html
<!DOCTYPE html>
<html lang="en">
<head>
<meta charset="utf-8">
<title>Quiet Venture Pathway – Information Session</title>
<link href="https://fonts.googleapis.com/css2?family=Oswald:wght@500;700&family=Playball&family=PT+Sans:wght@400;700&family=PT+Sans+Narrow:wght@400;700&family=Noto+Serif:wght@400;700&family=Carlito:ital,wght@0,400;0,700;1,400;1,700&family=Open+Sans:wght@400&family=Caveat:wght@700&display=swap" rel="stylesheet">
<style>
  :root{
    --white:#ffffff;
    --ink:#3b2320;
    --brown:#7b4426;
    --green:#acd037;
    --green-deep:#8fb52a;
    --orange:#f37122;
    --blue:#33a6d7;
    --blue-deep:#3a78b6;
    --grey-disc:#c9c9cc;
    --text-dark:#2c2c2c;
  }
  *{margin:0;padding:0;box-sizing:border-box}
  html,body{width:890px;height:1200px;overflow:hidden;background:var(--white)}
  body{position:relative;font-family:"Carlito",sans-serif;color:var(--text-dark)}
  .abs{position:absolute}

  /* ---------- Page 1 ---------- */
  .page-front{left:15px;top:15px;width:860px;height:573px;overflow:hidden}
  .forest-photo{left:0;top:0;width:860px;height:573px;
    background:linear-gradient(90deg,#3e4a24 0%,#6b6a3a 10%,#4e4a30 18%,#8c8a78 22%,#a9a89c 45%,#b7b5aa 70%,#a8a596 100%)}
  .forest-veil{left:172px;top:0;width:688px;height:573px;background:rgba(205,203,196,.55)}
  .title-main{left:196px;top:22px;width:660px;text-align:center;font-family:"Oswald",sans-serif;font-weight:700;
    font-size:62px;line-height:70px;letter-spacing:.5px;color:var(--ink);text-transform:uppercase}
  .title-script{left:360px;top:86px;width:440px;text-align:center;font-family:"Playball",cursive;font-size:80px;line-height:92px;color:var(--ink)}
  .title-sub{left:400px;top:162px;width:420px;text-align:center;font-family:"PT Sans",sans-serif;font-weight:700;font-size:34px;color:var(--brown)}
  .facilitator{left:304px;top:218px;font-family:"PT Sans",sans-serif;font-size:22px;color:var(--ink);letter-spacing:.3px}
  .facilitator b{font-weight:700;letter-spacing:1px}
  .bio{left:281px;top:258px;width:575px;font-size:9.8px;line-height:15.4px;color:var(--ink)}

  .portrait-frame{left:69px;top:169px;width:202px;height:328px;background:var(--green)}
  .portrait-photo{left:6px;top:6px;width:190px;height:241px;background:linear-gradient(180deg,#e4e2e4 0%,#d9d6d9 45%,#3d4b66 75%,#2c3850 100%)}
  .portrait-name{left:0;top:251px;width:202px;text-align:center;font-family:"Noto Serif",serif;font-weight:700;font-size:19px;color:var(--ink)}
  .portrait-role{left:0;top:280px;width:202px;text-align:center;font-family:"PT Sans",sans-serif;font-size:14.5px;letter-spacing:.6px;color:var(--ink)}
  .portrait-org{left:0;top:300px;width:202px;text-align:center;font-family:"Noto Serif",serif;font-size:16px;letter-spacing:.4px;color:var(--ink)}

  .details{left:281px;top:368px;width:355px}
  .detail{border-top:2px solid var(--ink);text-align:center;color:var(--ink);height:57px;padding-top:4px;white-space:nowrap}
  .detail:last-child{border-bottom:2px solid var(--ink);height:60px}
  .detail-label{font-family:"PT Sans",sans-serif;font-size:17px;line-height:22px;text-transform:uppercase}
  .detail-value{font-family:"Oswald",sans-serif;font-weight:500;font-size:20px;line-height:26px;letter-spacing:.3px}
  .detail:last-child .detail-value{font-family:"PT Sans Narrow",sans-serif;font-weight:700;font-size:18px;letter-spacing:0}

  .brand-front{left:652px;top:440px;width:205px;text-align:center}
  .brand-dot{width:62px;height:62px;border-radius:50%;background:var(--orange);margin:0 auto 10px}
  .brand-name{font-family:"Open Sans",sans-serif;font-size:24px;line-height:28px;color:var(--blue)}
  .brand-tag{font-family:"PT Sans Narrow",sans-serif;font-size:8.6px;letter-spacing:.4px;color:var(--ink);margin-top:2px}

  /* ---------- Page 2 ---------- */
  .page-inside{left:15px;top:614px;width:860px;height:575px;overflow:hidden}
  .sky-photo{left:0;top:0;width:224px;height:575px;
    background:linear-gradient(180deg,#6f9fce 0%,#a9c4e0 22%,#e2e8ee 45%,#cfd8e0 58%,#5d6d83 70%,#6b7f4e 80%,#8a8f45 92%,#7a7a55 100%)}
  .meadow-photo{left:224px;top:0;width:366px;height:575px;
    background:linear-gradient(180deg,#b9d36e 0%,#c7dc8a 45%,#a8c75c 70%,#8fb048 100%)}
  .ridge-photo{left:590px;top:0;width:270px;height:575px;
    background:linear-gradient(180deg,#9bbcd9 0%,#c8d7e4 30%,#d6dee4 55%,#c2ccd2 80%,#b2bcc2 100%)}
  .brand-inside{left:22px;top:30px;display:flex;align-items:center;gap:10px}
  .brand-inside .brand-dot{width:50px;height:50px;margin:0}
  .brand-inside .brand-name{font-size:24px;line-height:24px;color:var(--blue)}
  .contact{font-size:13px;color:var(--text-dark);display:flex;align-items:center;gap:8px;white-space:nowrap}
  .contact svg{flex:none}

  .mid-heading{left:249px;top:16px;font-family:"PT Sans",sans-serif;font-weight:700;font-size:16px;color:var(--brown);letter-spacing:.2px}
  .mid-lead{left:244px;top:41px;width:345px;font-size:12px;line-height:17.1px;color:var(--text-dark)}
  .mid-body{left:243px;top:156px;width:342px;font-size:10.5px;line-height:17px;color:var(--text-dark)}
  .cycle{left:224px;top:280px;width:366px;height:255px}
  .cycle text{font-family:"Carlito",sans-serif;text-anchor:middle}
  .tagline{left:224px;top:536px;width:366px;height:32px;display:flex;align-items:center;gap:10px}
  .tagline .rule{flex:1;height:1.5px;background:var(--ink)}
  .tagline span{font-family:"Caveat",cursive;font-weight:700;font-size:22px;color:var(--ink)}

  .side-heading{left:639px;font-family:"PT Sans",sans-serif;font-weight:700;font-size:21px;line-height:24px}
  .why{top:15px;color:var(--blue-deep)}
  .how{top:278px;color:var(--orange)}
  .side-text{left:606px;width:250px;font-size:10.9px;line-height:17px;color:var(--text-dark)}
  .side-list{list-style:none;left:601px;width:256px;font-size:10.9px;line-height:17px;color:var(--text-dark)}
  .side-list li{padding-left:11px;position:relative}
  .side-list li::before{content:"\2736";position:absolute;left:0;top:0;font-size:7px}
</style>
</head>
<body>

<section class="page-front abs" aria-label="Information session page">
  <div class="forest-photo abs" role="img" aria-label="Photo of a person walking along a forest path among tall pines"></div>
  <div class="forest-veil abs"></div>

  <h1 class="title-main abs">Quiet Venture</h1>
  <div class="title-script abs">Pathway</div>
  <div class="title-sub abs">Information Session</div>

  <p class="facilitator abs">FACILITATOR: <b>Dr. TOMAS VARELA</b></p>
  <p class="bio abs">Tomas joined Northfield University (School of Management) as a Lecturer in Entrepreneurship in 2015. He completed his PhD in Entrepreneurship at Kelburn Business School in 2014. His work received the Alder Doctoral Dissertation Award from the Guild of Management Studies. He began his business career as a production engineer (Voltrex), and continued in sales (Heimwerk). After his MBA, he worked as a strategy consultant at Douro Business School. Originally from Portugal, Tomas enjoys designing and launching new ideas, international communities, mindfulness retreats, and musical improvisation. He nurtures a close connection to Cedar Hollow Mindfulness Centre, where he has practiced and volunteered over 9 months. He has a broad experience of sharing the benefits of mindfulness with others.</p>

  <div class="portrait-frame abs">
    <div class="portrait-photo abs" role="img" aria-label="Portrait photo of the facilitator in a blue blazer and scarf"></div>
    <div class="portrait-name abs">Dr.TOMAS VARELA</div>
    <div class="portrait-role abs">Visiting Research Fellow</div>
    <div class="portrait-org abs">Northfield University</div>
  </div>

  <div class="details abs">
    <div class="detail"><div class="detail-label">Date</div><div class="detail-value">SEPTEMBER 05, 2019</div></div>
    <div class="detail"><div class="detail-label">Time</div><div class="detail-value">19.30 - 21.00</div></div>
    <div class="detail"><div class="detail-label">Venue</div><div class="detail-value">Tidewater Coworking, C/ Almendro 42, Barcelona</div></div>
  </div>

  <div class="brand-front abs">
    <div class="brand-dot"></div>
    <div class="brand-name">bright meadow</div>
    <div class="brand-tag">Calm, Craft and Enterprise for Joyful Living</div>
  </div>
</section>

<section class="page-inside abs" aria-label="About the pathway page">
  <div class="sky-photo abs" role="img" aria-label="Photo of a blue sky with white clouds above distant mountains and a grassy hillside"></div>
  <div class="meadow-photo abs" role="img" aria-label="Photo of a green mountain meadow under a soft light"></div>
  <div class="ridge-photo abs" role="img" aria-label="Photo of pale mountain ridges under a hazy sky"></div>

  <div class="brand-inside abs">
    <div class="brand-dot"></div>
    <div class="brand-name">bright<br>meadow</div>
  </div>

  <div class="contact abs" style="top:237px;left:32px">
    <svg width="22" height="18" viewBox="0 0 22 18" aria-hidden="true"><rect x="1" y="2" width="20" height="15" rx="1.5" fill="#f3c04d"/><path d="M1 3 L11 11 L21 3" fill="none" stroke="#c9892a" stroke-width="1.4"/></svg>
    <span>info@brightmeadow.example</span>
  </div>
  <div class="contact abs" style="top:264px;left:48px">
    <svg width="22" height="22" viewBox="0 0 22 22" aria-hidden="true"><circle cx="11" cy="11" r="10.5" fill="var(--green-deep)"/><path d="M7.5 6.2c.6-.5 1.4-.4 1.8.2l.9 1.5c.3.5.2 1.1-.2 1.5l-.6.5c.5 1.2 1.5 2.2 2.7 2.7l.5-.6c.4-.4 1-.5 1.5-.2l1.5.9c.6.4.7 1.2.2 1.8l-.7.8c-.6.6-1.5.8-2.300.4-2.7-1.2-4.8-3.3-6-6-.4-.8-.2-1.7.4-2.3z" fill="#fff"/></svg>
    <span>+34 600 000 123</span>
  </div>

  <h2 class="mid-heading abs">What is Mindful Entrepreneurship?</h2>
  <p class="mid-lead abs">Being mindful means being aware and awake.<br>Entrepreneurship is the creation of a new form of organising.<br>Mindful Entrepreneurship is then the process of creating or<br>redesigning your work and life with awareness,<br>in a way that is reflective of you, of your passions and values,<br>thus conducing to a greater sense of fulfilment and happiness.</p>
  <p class="mid-body abs">The Quiet Venture Pathway is a 4-month long transformative journey designed for people who feel stuck or not entirely satisfied with their professional and/or personal life. It will be of benefit for everyone, at any stage.<br>The Program consists of a 5-hour workshop every month, complemented by 2-hour weekly peer support meetings. It combines mindfulness techniques, design thinking methodology, and entrepreneurship frameworks.</p>

  <svg class="cycle abs" viewBox="0 0 366 255" aria-label="Four workshops joined in a cycle by weekly peer support meetings">
    <defs>
      <marker id="head" markerUnits="userSpaceOnUse" markerWidth="11" markerHeight="11" refX="4" refY="5.5" orient="auto"><path d="M0 0 L11 5.5 L0 11z" fill="context-stroke"/></marker>
    </defs>
    <g stroke-width="4" fill="none" stroke-linecap="round">
      <path d="M221 72 L233 84" stroke="var(--green)" marker-end="url(#head)"/>
      <path d="M240 161 L228 173" stroke="var(--blue)" marker-end="url(#head)"/>
      <path d="M134 187 L122 175" stroke="var(--orange)" marker-end="url(#head)"/>
      <path d="M115 85 L127 73" stroke="var(--grey-disc)" marker-end="url(#head)"/>
    </g>
    <circle cx="178" cy="47" r="44" fill="var(--green)"/>
    <circle cx="273" cy="124" r="44" fill="var(--blue)"/>
    <circle cx="178" cy="202" r="44" fill="var(--orange)"/>
    <circle cx="89" cy="124" r="44" fill="var(--grey-disc)"/>
    <g fill="#fff">
      <text x="178" y="36" font-size="10">Workshop 1</text><text x="178" y="50" font-size="11.5" font-weight="700">INSIGHT</text><text x="178" y="63" font-size="9.5" font-style="italic">(5 hours)</text>
      <text x="273" y="113" font-size="10">Workshop 2</text><text x="273" y="127" font-size="11.5" font-weight="700">DESIGN</text><text x="273" y="140" font-size="9.5" font-style="italic">(5 hours)</text>
      <text x="178" y="191" font-size="10">Workshop 3</text><text x="178" y="205" font-size="11.5" font-weight="700">EXECUTE</text><text x="178" y="218" font-size="9.5" font-style="italic">(5 hours)</text>
      <text x="89" y="113" font-size="10">Workshop 4</text><text x="89" y="127" font-size="11.5" font-weight="700">PRESENT</text><text x="89" y="140" font-size="9.5" font-style="italic">(5 hours)</text>
    </g>
    <g fill="#444" font-size="9.5" font-style="italic">
      <text x="276" y="44">Weekly Peer Support</text><text x="276" y="56">(WPS) meetings</text><text x="276" y="68">(2 hours)</text>
      <text x="86" y="64">WPS meetings</text>
      <text x="86" y="202">WPS meetings</text>
      <text x="272" y="202">WPS meetings</text>
    </g>
  </svg>

  <div class="tagline abs"><div class="rule"></div><span>The way out is in</span><div class="rule"></div></div>

  <h2 class="side-heading why abs">WHY</h2>
  <p class="side-text abs" style="top:38px">Many people are not satisfied with their work or life, but they don’t know what to do about it.<br>This Program offers you a safe place to conduct your inner journey with collective support, helping you reflect, design, and (very likely) do something about it. It aims at:</p>
  <ul class="side-list abs" style="top:157px">
    <li>Increasing awareness, clarity and confidence</li>
    <li>Having a deeper insight on what makes you happier and what you want</li>
    <li>Developing a clear design integrating your intended work and life</li>
    <li>Start executing this design.</li>
  </ul>

  <h2 class="side-heading how abs">HOW</h2>
  <p class="side-text abs" style="top:301px">This Program differs from existing entrepreneurial programs in many ways:</p>
  <ul class="side-list abs" style="top:352px;left:603px;width:254px">
    <li>Uses mindfulness and self analysis to look deeply into yourself</li>
    <li>Design and execution decisions are based on happiness rather than (only) financials</li>
    <li>Holistic and inclusive design process, integrating work and life, and building synergies between your different parts.</li>
  </ul>
  <p class="side-text abs" style="top:489px">The Program format includes lectures, individual work, group sharing, guided activities, experiential exercises, video, audio, handouts and other resources.</p>
</section>

</body>
</html>
```